Wholesaler needs a bag design for cassava flour

I need design for a package bag to pack cassava flour (white powder). This flower is made from manioc and is very much used by African countries. I want to make packages of 0.5kg with 160mm base to 230mm height. I would like ta package to have clear parts so that customers can see the quality of the product. The brand name of the product is " MIRAVO " and the name of the product in Portuguese is "Fuba de Bombó". I want the design to be simple not many colors and attractive.
The design should have a front page and a back page. The front side I would like to have the brand, the name of the product and a simple design while on the back side it should have the space to fill with the nutrition facts, our company information, bar code and other information demanded by EU regulation
African Communities in Portugal
Wholesale

```html
<!DOCTYPE html>
<html lang="en">
<head>
<meta charset="utf-8">
<title>MIRAVO – Fuba de Bombó pouch front</title>
<link rel="stylesheet" href="https://fonts.googleapis.com/css2?family=Questrial&display=swap">
<style>
  :root {
    --backdrop: #ececec;
    --pouch-white: #ffffff;
    --brand-green: #3fae3a;
    --light-green: #9ccc3c;
    --brand-brown: #5a3418;
    --text-brown: #6b4a35;
    --flour-light: #e9e2e0;
    --flour-mid: #d3c8c6;
  }
  * { box-sizing: border-box; margin: 0; padding: 0; }
  html, body { width: 1200px; height: 1000px; overflow: hidden; }
  body {
    background: var(--backdrop);
    font-family: "Questrial", sans-serif;
    position: relative;
  }
  .pouch {
    position: absolute;
    left: 385px; top: 135px;
    width: 430px; height: 725px;
    background: var(--pouch-white);
    border-radius: 6px;
    overflow: hidden;
    box-shadow: 0 10px 30px rgba(0,0,0,0.12);
  }
  .pouch-top {
    position: absolute; left: 0; top: 0;
    width: 430px; height: 290px;
  }
  .brand-band {
    position: absolute;
    left: 150px; top: 0;
    width: 130px; height: 195px;
    background: var(--pouch-white);
    display: flex; flex-direction: column; align-items: center;
  }
  .brand-dot {
    margin-top: 76px;
    width: 56px; height: 56px;
    border: 3px solid var(--brand-green);
    border-radius: 50%;
  }
  .brand-name {
    margin-top: 14px;
    font-size: 23px;
    letter-spacing: 1px;
    color: var(--brand-brown);
  }
  .product-title {
    position: absolute; left: 0; width: 100%;
    top: 298px;
    text-align: center;
    font-size: 30px;
    letter-spacing: 7px;
    color: var(--brand-green);
  }
  .product-subtitle {
    position: absolute; left: 0; width: 100%;
    top: 337px;
    text-align: center;
    font-size: 17px;
    letter-spacing: 2.4px;
    color: var(--light-green);
  }
  .clear-window {
    position: absolute;
    left: 25px; top: 390px;
    width: 380px; height: 242px;
    border-radius: 50%;
    background: radial-gradient(ellipse at 45% 40%, var(--flour-light), var(--flour-mid));
  }
  .claims {
    position: absolute; left: 0; width: 100%;
    top: 635px;
    text-align: center;
    font-size: 12px;
    color: var(--text-brown);
  }
  .net-weight {
    position: absolute; left: 0; width: 100%;
    top: 673px;
    text-align: center;
    font-size: 13px;
    color: var(--text-brown);
  }
</style>
</head>
<body>
  <div class="pouch">
    <svg class="pouch-top" viewBox="0 0 430 290" aria-hidden="true">
      <path d="M0 0 H430 V275 Q250 212 0 230 Z" fill="var(--brand-green)"/>
    </svg>
    <div class="brand-band">
      <div class="brand-dot"></div>
      <div class="brand-name">MIRAVO</div>
    </div>
    <h1 class="product-title">FUBA DE BOMBÓ</h1>
    <p class="product-subtitle">%100 African Cassava Flour</p>
    <div class="clear-window" role="img" aria-label="Clear window showing the white cassava flour inside"></div>
    <p class="claims">Gluten free - Grain free - Nut free - %100 Yuca Root</p>
    <p class="net-weight">500 gr</p>
  </div>
</body>
</html>
```